Event Program Design

We are looking to create a stunning event program for “Velvet Gala Night,” presented by The Marlow Chamber Society. This program will reflect the upscale theme of the event while maintaining a clean, elegant layout. We will use a past year’s program as a reference to replicate a similar structure and overall flow, including all page layouts. The cover design will incorporate both front and back, with an inside cover that carries through the sophisticated look established on the front.
Because there are 31 individuals to feature, along with group photos, the program will require enough pages to accommodate everyone without feeling overcrowded (use previous design for reference).
We also have inspirational images and the event invitation available for reference. Please note that these images are for layout purposes only and should not be used for any design elements in the new design—they are solely meant to inspire the final product’s style and color palette.
We plan to base the program’s color scheme on the invitation’s aesthetic; however, we want to avoid directly copying any design features from the reference images or the previous year’s sample. Font selections should complement the elegant theme and must be free to download and use commercially.
The new design should set up for 8 x 11 print size, full color. Please include adequate bleed for print. Will be using prindle for printing so please contact them for any additional questions.
Our goal is a cohesive, refined program that helps attendees navigate the evening’s events while reflecting the grandeur of The Marlow Chamber Society’s “Velvet Gala Night.” We look forward to a layout that strikes the perfect balance between classic sophistication and modern flair—something as memorable as the event itself.

```html
<!DOCTYPE html>
<html lang="en">
<head>
<meta charset="utf-8">
<title>Velvet Gala Night – Program Spreads</title>
<link href="https://fonts.googleapis.com/css2?family=Great+Vibes&family=Cormorant+Garamond:wght@500;600&family=Arimo:wght@400&display=swap" rel="stylesheet">
<style>
  :root{
    --canvas:#dedede;
    --paper:#ffffff;
    --pink:#e2378e;
    --pink-soft:#f4c7e4;
    --pink-mist:#fbe6f3;
    --violet:#7d2a9c;
    --violet-soft:#b57fd2;
    --plum-night:#2b0d33;
    --ink:#2a2a2a;
    --ink-soft:#555;
    --script:"Great Vibes", cursive;
    --serif:"Cormorant Garamond", serif;
    --sans:"Arimo", sans-serif;
  }
  *{box-sizing:border-box;margin:0;padding:0}
  html,body{width:1200px;height:840px;overflow:hidden;background:var(--canvas)}
  .sheet{position:relative;width:1200px;height:840px}
  .page{position:absolute;width:266px;height:366px;background:var(--paper);overflow:hidden;box-shadow:0 1px 3px rgba(0,0,0,.12)}
  .row-top{top:49px}.row-bottom{top:434px}
  .col-1{left:48px}.col-2{left:333px}.col-3{left:613px}.col-4{left:897px}
  .abs{position:absolute}
  .floral{position:absolute}
  .ornament{position:absolute;border-radius:50%;background:radial-gradient(circle at 40% 35%,#f9b6dc,#d63b93 55%,#7d2a9c)}
  .script{font-family:var(--script);font-weight:400;line-height:1}
  .serif-caps{font-family:var(--serif);font-weight:600;text-transform:uppercase;color:var(--violet);text-align:center;line-height:1}
  .center{left:0;right:0;text-align:center}

  /* cover */
  .cover-floral{inset:0;background:radial-gradient(ellipse 62% 55% at 50% 50%,#fff 55%,#f7c3e1 78%,#e86aae 92%,#a45bc7 100%)}
  .cover-title{top:128px;font-size:50px}
  .cover-title .line-a{color:var(--pink);display:block}
  .cover-title .line-b{color:var(--violet);display:block;margin-top:4px}
  .cover-society{top:247px;font-size:16px;padding:0 50px}

  /* schedule */
  .band-top{left:0;right:0;top:0;height:140px;background:linear-gradient(180deg,#f06bb1,#f7a9d3 55%,#fbe0f0)}
  .side-frame{top:140px;bottom:0;width:14px;background:var(--pink-soft)}
  .bottom-frame{left:0;right:0;bottom:0;height:16px;background:var(--pink-soft)}
  .date-bar{top:143px;left:50px;width:160px;height:26px;background:linear-gradient(90deg,#7d2a9c,#c23a9a);color:#fff;font-family:var(--serif);font-size:17px;font-weight:600;display:flex;align-items:center;justify-content:center;letter-spacing:.5px}
  .slot{position:absolute;left:0;right:0;text-align:center;font-family:var(--sans);color:var(--ink)}
  .slot .time{font-size:11px;color:var(--violet)}
  .slot .desc{font-size:6.3px;line-height:8px;margin-top:2px}

  /* bios */
  .bio-heading{top:12px;left:80px;font-size:30px;color:var(--pink)}
  .portrait{position:absolute;border-radius:50%;border:3px solid #fff;box-shadow:0 0 0 2px #f08cc2;background:linear-gradient(160deg,#c9a58f,#8e6a5a 60%,#e6dba0)}
  .belle-name{font-family:var(--sans);color:var(--pink);text-align:center;line-height:1.1}
  .belle-name .first{font-size:10px}
  .belle-name .rest{font-size:11px;color:var(--violet)}
  .bio{position:absolute;font-family:var(--sans);font-size:5.6px;line-height:6.9px;color:var(--ink);text-align:justify}

  /* roster page */
  .roster-frame{inset:0;background:linear-gradient(135deg,#f7c8e5,#fbe4f2 45%,#f5c2e2)}
  .roster-panel{left:12px;right:12px;top:14px;bottom:14px;background:#fff;border-radius:10px}
  .roster-society{top:72px;font-size:19px;line-height:19px}
  .roster-script{top:138px;font-size:32px;color:var(--pink)}
  .name-list{position:absolute;left:0;right:0;top:184px;list-style:none;text-align:center;font-family:var(--sans);font-size:10.5px;line-height:16.7px;color:var(--ink-soft)}

  /* seniors group */
  .page-blush{background:var(--pink-soft)}
  .seniors-head{top:20px;font-size:30px;color:var(--pink)}
  .group-bloom{left:40px;top:80px;width:186px;height:220px;border-radius:40%;background:radial-gradient(ellipse at center,#e86aae 30%,#f08fc6 55%,rgba(244,199,228,0) 75%)}
  .photo-frame{position:absolute;background:#fff;padding:4px}
  .photo-fill{width:100%;height:100%}
  .caption{position:absolute;left:0;right:0;text-align:center;font-family:var(--sans);font-size:6.4px;line-height:7.8px;color:var(--ink)}

  /* juniors */
  .juniors-frame{inset:0;background:linear-gradient(180deg,#f3b2d8 0%,#fbe3f1 22%,#fbe3f1 70%,#f07db9 100%)}
  .juniors-panel{left:14px;right:14px;top:16px;bottom:30px;background:#fff}
  .juniors-head{top:50px;font-size:30px;color:var(--pink)}
  .body-copy{position:absolute;left:24px;right:28px;font-family:var(--sans);font-size:5.6px;line-height:6.8px;color:var(--ink);text-align:justify}
  .body-copy p+p{margin-top:5px}
  .juniors-bloom{right:0;bottom:0;width:80px;height:46px;border-radius:60% 0 0 0;background:radial-gradient(circle at 85% 90%,#e2378e 25%,#f39ccb 55%,rgba(243,156,203,0) 80%)}

  /* belle list */
  .belle-base{left:0;right:0;bottom:0;height:210px;background:linear-gradient(180deg,#fff,#f7b6da 80%,#ee70b3)}
  .belle-top{left:0;right:0;top:0;height:62px;background:linear-gradient(180deg,#e94f9f,#f5a7d1 70%,#fff)}
  .belle-panel{left:10px;right:10px;top:60px;bottom:12px;background:#fff}
  .belle-ghost{left:78px;top:150px;width:110px;height:185px;border-radius:50% 50% 40% 40%;background:radial-gradient(circle,rgba(190,170,210,.28),rgba(190,170,210,0) 70%)}
  .belle-society{top:72px;font-size:14px;letter-spacing:.3px}
  .belle-script{top:96px;font-size:30px;color:var(--pink)}
  .belle-col{position:absolute;top:134px;list-style:none;font-family:var(--sans);font-size:8.4px;line-height:12.4px;color:var(--ink)}

  /* back cover */
  .page-night{background:var(--plum-night)}
  .night-floral{inset:0;background:radial-gradient(ellipse 58% 52% at 50% 50%,var(--plum-night) 60%,#6a1f6b 80%,#e0479a 100%)}
  .night-title{top:180px;font-size:34px;line-height:34px;color:#ee58a8}
  .night-web{top:266px;font-family:var(--serif);font-size:11px;line-height:12px;color:#fff;letter-spacing:.6px}
</style>
</head>
<body>
<main class="sheet">

  <!-- Front cover -->
  <section class="page row-top col-1 cover">
    <div class="floral cover-floral" role="img" aria-label="Hand-drawn pink and violet floral border surrounding the page"></div>
    <div class="ornament" style="left:110px;top:80px;width:46px;height:46px" role="img" aria-label="Mirror ball ornament illustration"></div>
    <h1 class="abs center script cover-title"><span class="line-a">Velvet Gala</span><span class="line-b">Night</span></h1>
    <p class="abs center serif-caps cover-society">Marlow Chamber Society</p>
  </section>

  <!-- Schedule -->
  <section class="page row-top col-2 schedule">
    <div class="floral band-top" role="img" aria-label="Large pink and violet flower illustrations across the top"></div>
    <div class="abs side-frame" style="left:0"></div>
    <div class="abs side-frame" style="right:0"></div>
    <div class="abs bottom-frame"></div>
    <div class="abs date-bar">8 JANUARY 2025</div>
    <div class="slot" style="top:183px"><p class="time">8:30 PM</p><p class="desc">Lorem ipsum dolor sit amet, consectetur adipiscing elit.</p></div>
    <div class="slot" style="top:216px"><p class="time">8:30 PM</p><p class="desc">Lorem ipsum dolor sit amet, consectetur adipiscing elit.<br>Lorem ipsum dolor sit amet, consectetur adipiscing elit.</p></div>
    <div class="slot" style="top:258px"><p class="time">8:30 PM</p><p class="desc">Lorem ipsum dolor sit amet, consectetur adipiscing elit.</p></div>
    <div class="ornament" style="left:113px;top:293px;width:40px;height:40px" role="img" aria-label="Mirror ball ornament illustration"></div>
  </section>

  <!-- Senior bios -->
  <section class="page row-top col-3 bios" style="background:#fffafd">
    <h2 class="abs script bio-heading">Seniors</h2>
    <div class="floral" style="left:0;top:48px;width:120px;height:150px;border-radius:45%;background:radial-gradient(circle,#f7a6d1 30%,rgba(247,166,209,0) 72%)" role="img" aria-label="Pink floral wreath illustration"></div>
    <div class="portrait" style="left:6px;top:62px;width:80px;height:80px" role="img" aria-label="Portrait photo of senior belle Clara Juliet Haven"></div>
    <div class="ornament" style="left:95px;top:160px;width:26px;height:26px" role="img" aria-label="Mirror ball ornament illustration"></div>
    <div class="abs belle-name" style="left:140px;width:120px;top:36px"><p class="first">CLARA</p><p class="rest">Juliet Haven</p></div>
    <p class="bio" style="left:133px;width:120px;top:62px">Clara Juliet Haven, 17, is the daughter of Mr. and Mrs. Daniel Haven. She is a four year varsity golfer, a member of the National Honor Society and a volunteer with local meal programs. Clara has been a Marlow Chamber Society Belle for four years. She plans to study business in the fall and keep playing golf.</p>
    <div class="abs belle-name" style="left:13px;width:122px;top:204px"><p class="first">CLARA</p><p class="rest">Juliet Haven</p></div>
    <p class="bio" style="left:13px;width:122px;top:230px">Clara Juliet Haven, 17, is the daughter of Mr. and Mrs. Daniel Haven. She is a four year varsity golfer, a member of the National Honor Society and a volunteer with local meal programs. Clara has been a Marlow Chamber Society Belle for four years. She plans to study business in the fall and keep playing golf.</p>
    <div class="floral" style="left:140px;top:220px;width:126px;height:130px;border-radius:45%;background:radial-gradient(circle,#f7a6d1 30%,rgba(247,166,209,0) 72%)" role="img" aria-label="Pink floral wreath illustration"></div>
    <div class="portrait" style="left:176px;top:242px;width:80px;height:80px" role="img" aria-label="Portrait photo of senior belle Clara Juliet Haven"></div>
  </section>

  <!-- Senior Belle roster -->
  <section class="page row-top col-4 roster">
    <div class="floral roster-frame" role="img" aria-label="Pink floral and heart border illustration"></div>
    <div class="abs roster-panel"></div>
    <div class="floral" style="left:0;bottom:0;width:266px;height:90px;background:linear-gradient(180deg,rgba(255,255,255,0),#f39ccb 60%,#e2378e)" role="img" aria-label="Pink chrysanthemum illustrations along the bottom"></div>
    <div class="ornament" style="left:201px;top:40px;width:40px;height:40px" role="img" aria-label="Mirror ball ornament illustration"></div>
    <p class="abs center serif-caps roster-society">Marlow<br>Chamber<br>Society</p>
    <p class="abs center script roster-script">Senior Belle</p>
    <ul class="name-list">
      <li>Name Surname</li><li>Name Surname</li><li>Name Surname</li>
      <li>Name Surname</li><li>Name Surname</li><li>Name Surname</li>
    </ul>
  </section>

  <!-- Seniors group -->
  <section class="page row-bottom col-1 page-blush seniors-group">
    <div class="ornament" style="left:16px;top:20px;width:40px;height:40px" role="img" aria-label="Mirror ball ornament illustration"></div>
    <div class="ornament" style="left:210px;top:20px;width:40px;height:40px" role="img" aria-label="Mirror ball ornament illustration"></div>
    <h2 class="abs center script seniors-head">Seniors</h2>
    <div class="floral group-bloom" role="img" aria-label="Pink and violet floral wreath illustration"></div>
    <div class="photo-frame" style="left:88px;top:106px;width:105px;height:160px">
      <div class="photo-fill" style="background:linear-gradient(180deg,#6b5a52,#3c2e2b 55%,#b79ac9)" role="img" aria-label="Group photo of the senior belles in gowns on a staircase"></div>
    </div>
    <p class="caption" style="top:321px">From left to right:<br>Name Surname, Name Surname, Name Surname<br>Name Surname, Name Surname, Name Surname<br>Name Surname, Name Surname, Name Surname<br>Name Surname, Name Surname, Name Surname</p>
  </section>

  <!-- Juniors -->
  <section class="page row-bottom col-2 juniors">
    <div class="floral juniors-frame" role="img" aria-label="Pink and violet floral border illustration"></div>
    <div class="abs juniors-panel"></div>
    <div class="ornament" style="left:200px;top:42px;width:34px;height:34px" role="img" aria-label="Mirror ball ornament illustration"></div>
    <h2 class="abs center script juniors-head">Juniors</h2>
    <div class="abs" style="left:22px;top:84px;width:216px;height:145px;background:linear-gradient(180deg,#c9d6dd,#9aa57a 50%,#2a2a2a 75%,#6b6b4f)" role="img" aria-label="Group photo of the junior members outdoors by a windmill"></div>
    <div class="body-copy" style="top:240px">
      <p>Lorem ipsum dolor sit amet, consectetur adipiscing elit. Sed volutpat pretium pharetra. Maecenas porta diam justo, vitae hendrerit nisi commodo et. Quisque eu metus condimentum, suscipit augue nec, hendrerit enim.</p>
      <p>Phasellus rutrum, libero eu consequat semper, felis libero vestibulum odio, sit amet dignissim nulla tortor at urna. Nunc dignissim ullamcorper urna, non vulputate dolor interdum sed.</p>
    </div>
    <div class="floral juniors-bloom" role="img" aria-label="Pink chrysanthemum illustration"></div>
  </section>

  <!-- Senior Belle list -->
  <section class="page row-bottom col-3 belle-list">
    <div class="floral belle-top" role="img" aria-label="Pink and violet flower illustrations across the top"></div>
    <div class="abs belle-base"></div>
    <div class="abs belle-panel"></div>
    <div class="floral belle-ghost" role="img" aria-label="Faint mirror ball illustration"></div>
    <p class="abs center serif-caps belle-society">Marlow Chamber Society</p>
    <p class="abs center script belle-script">Senior Belle</p>
    <ul class="belle-col" style="left:50px">
      <li>Name Surname</li><li>Name Surname</li><li>Name Surname</li><li>Name Surname</li>
      <li>Name Surname</li><li>Name Surname</li><li>Name Surname</li><li>Name Surname</li>
      <li>Name Surname</li><li>Name Surname</li><li>Name Surname</li><li>Name Surname</li>
      <li>Name Surname</li><li>Name Surname</li><li>Name Surname</li><li>Name Surname</li>
    </ul>
    <ul class="belle-col" style="left:171px">
      <li>Name Surname</li><li>Name Surname</li><li>Name Surname</li><li>Name Surname</li>
      <li>Name Surname</li><li>Name Surname</li><li>Name Surname</li><li>Name Surname</li>
      <li>Name Surname</li><li>Name Surname</li><li>Name Surname</li><li>Name Surname</li>
      <li>Name Surname</li><li>Name Surname</li><li>Name Surname</li><li>Name Surname</li>
    </ul>
  </section>

  <!-- Back cover -->
  <section class="page row-bottom col-4 page-night back-cover">
    <div class="floral night-floral" role="img" aria-label="Pink and lilac floral border on deep plum"></div>
    <div class="abs" style="left:93px;top:78px;width:80px;height:80px;border-radius:50%;background:radial-gradient(circle at 40% 35%,#7a6a86,#3f2a4a 70%)" role="img" aria-label="Line-drawn mirror ball illustration"></div>
    <p class="abs center script night-title">Velvet Gala<br>Night</p>
    <p class="abs center night-web">WWW.WEBSITE.COM</p>
  </section>

</main>
</body>
</html>
```